Ambo postcard design

I am in charge of getting a postcard 5x7 designed for 14 artists having a gallery exhibition. We would like to use our
photo(s) with the 14 names on the front. Back of card would have gallery information.
Am sending jpeg of a past card, four images to choose from and the text for back of card.

```html
<!DOCTYPE html>
<html lang="en">
<head>
<meta charset="utf-8">
<title>Ambo Gallery – Fourteen Painters Postcard</title>
<link rel="stylesheet" href="https://fonts.googleapis.com/css2?family=Arimo:wght@400;700&family=Oswald:wght@300;400&display=swap">
<style>
  :root {
    --paper: #ffffff;
    --ink: #1a1f24;
    --black: #000000;
    --band: rgba(255, 255, 255, 0.62);
    --paint-black: #0b0b10;
    --paint-yellow: #f2dc1a;
    --paint-red: #e0252b;
    --paint-blue: #2f2bb8;
    --paint-cyan: #1fa9e6;
    --paint-orange: #f58a12;
  }
  * { box-sizing: border-box; margin: 0; padding: 0; }
  html, body { width: 1200px; height: 1000px; overflow: hidden; background: var(--paper); }
  .canvas { position: relative; width: 1200px; height: 1000px; }

  .card-front {
    position: absolute; left: 337px; top: 99px; width: 526px; height: 376px; overflow: hidden;
  }
  .card-front__photo {
    position: absolute; inset: 0;
    background:
      radial-gradient(ellipse 40% 35% at 75% 30%, rgba(224,37,43,0.75), transparent 70%),
      radial-gradient(ellipse 35% 30% at 55% 55%, rgba(47,43,184,0.8), transparent 70%),
      radial-gradient(ellipse 40% 30% at 20% 25%, rgba(242,220,26,0.7), transparent 70%),
      radial-gradient(ellipse 40% 30% at 85% 75%, rgba(242,220,26,0.6), transparent 70%),
      radial-gradient(ellipse 35% 25% at 30% 80%, rgba(31,169,230,0.6), transparent 70%),
      radial-gradient(ellipse 25% 20% at 55% 85%, rgba(245,138,18,0.6), transparent 70%),
      var(--paint-black);
  }
  .card-front__band {
    position: absolute; left: 45px; top: 0; width: 101px; height: 100%;
    background: var(--band);
    font-family: "Oswald", "Arial Narrow", sans-serif;
    color: var(--black); text-align: center; text-transform: uppercase;
  }
  .artist-list { list-style: none; font-size: 11px; line-height: 15px; font-weight: 300; }
  .artist-list--top { margin-top: 45px; }
  .show-title { font-size: 16.5px; line-height: 26px; font-weight: 300; margin: 12px 0 10px; }

  .card-back {
    position: absolute; left: 331px; top: 500px; width: 531px; height: 380px;
    border: 1px solid var(--ink); background: var(--paper);
  }
  .card-back__info {
    position: absolute; left: 0; top: 60px; width: 265px;
    font-family: "Arimo", Arial, sans-serif; color: var(--ink); text-align: center;
  }
  .gallery-name { font-size: 16px; font-weight: 400; letter-spacing: 0.2px; line-height: 20px; }
  .gallery-rule { width: 172px; height: 1px; background: var(--ink); margin: 1px auto 2px; }
  .presents { font-size: 9.5px; line-height: 12px; }
  .by { font-size: 9.5px; line-height: 12px; margin-top: 3px; }
  .group-name { font-size: 16px; font-weight: 700; line-height: 18px; }
  .details { font-size: 6.3px; font-weight: 700; line-height: 10.5px; margin-top: 14px; }
  .details + .details { margin-top: 10px; }

  .card-back__divider { position: absolute; left: 264px; top: 29px; width: 1px; height: 322px; background: var(--ink); }
  .stamp-box { position: absolute; left: 439px; top: 36px; width: 53px; height: 71px; border: 1px solid var(--ink); }
  .address-lines { position: absolute; left: 302px; top: 0; width: 190px; }
  .address-line { position: absolute; left: 0; width: 190px; height: 1px; background: var(--ink); }
</style>
</head>
<body>
<main class="canvas">
  <section class="card-front">
    <div class="card-front__photo" role="img" aria-label="Close-up photograph of paint brushes lying on dripped black, yellow, red, blue and cyan paint"></div>
    <div class="card-front__band">
      <ul class="artist-list artist-list--top">
        <li>Barlow</li><li>Corwin</li><li>Castell</li><li>Cady</li><li>Dane</li><li>Greenholt</li><li>Jarvis</li>
      </ul>
      <h1 class="show-title">Fourteen<br>Painters</h1>
      <ul class="artist-list">
        <li>Kell</li><li>Linwood</li><li>Noble</li><li>Nystrom</li><li>Orrin</li><li>Roe</li><li>Shelton</li>
      </ul>
    </div>
  </section>

  <section class="card-back">
    <div class="card-back__info">
      <h2 class="gallery-name">AMBO GALLERY</h2>
      <div class="gallery-rule"></div>
      <p class="presents">PRESENTS AN EXHIBITION</p>
      <p class="by">BY</p>
      <p class="group-name">“THE WREN GROUP”</p>
      <p class="details">SEPTEMBER 28TH – OCTOBER 31, 2015<br>RECEPTION – FRIDAY, OCTOBER 2, 5-8PM</p>
      <p class="details">AMBO GALLERY<br>LINDEN COURT SHOPS, 410 HARBOR LANE<br>FAIRVIEW, VIRGINIA 22090<br>555-014-2290<br>INFO@AMBOGALLERY.EXAMPLE<br>WWW.AMBOGALLERY.EXAMPLE</p>
      <p class="details">GALLERY HOURS: M-F 10:00AM-6:00PM<br>SATURDAY 10:00AM-2PM.<br>PARKING IS AVAILABLE IN<br>METERED SPOTS ON NEARBY STREETS<br>AND IN PUBLIC GARAGES.<br>(FREE ON WEEKENDS AND AFTER 4PM WEEKDAYS)</p>
    </div>
    <div class="card-back__divider"></div>
    <div class="stamp-box"></div>
    <div class="address-lines">
      <span class="address-line" style="top:163px"></span>
      <span class="address-line" style="top:193px"></span>
      <span class="address-line" style="top:223px"></span>
      <span class="address-line" style="top:254px"></span>
      <span class="address-line" style="top:284px"></span>
      <span class="address-line" style="top:315px"></span>
    </div>
  </section>
</main>
</body>
</html>
```